UK vitamin company needs a packaging label design for new vitamin range

We have a logo, and we have the product. We now need some beautiful labels to go on the boxes which bring the product range to life.
We have 7 categories: Joint Care, Heart Heath, Brain Function, Immune System, Skin, Antioxidants and Probiotics. Each of these categories should have its own look within the plumble tonic range. This can be quite subtle, but needs to be clearly visible and should be linked to the category e.g. 'Heart Health' might have a heart etc.
I have uploaded the logo, an example of the pack shape, and the sizing info for the label.
We are a fun brand, so please have some fun with this. We want the labels to be bold, and differentiated from the rest of the category.
Thanks
All images used must be 'rights free'. Many thanks
UK
It Company

```html
<!DOCTYPE html>
<html lang="en">
<head>
<meta charset="utf-8">
<title>plumble tonic – Heart Heath label</title>
<link href="https://fonts.googleapis.com/css2?family=Montserrat:wght@600&family=Oswald:wght@400;500&family=Questrial&display=swap" rel="stylesheet">
<style>
  :root {
    --backdrop: #000000;
    --paper: #ffffff;
    --leaf-green: #21a84a;
    --badge-green: #1f9a45;
    --accent-orange: #f47c20;
    --ink-grey: #6d6e71;
    --soft-grey: #8a8b8e;
  }
  html, body {
    margin: 0;
    padding: 0;
    width: 960px;
    height: 1200px;
    overflow: hidden;
    background: var(--backdrop);
  }
  .label {
    position: absolute;
    left: 139px;
    top: 170px;
    width: 680px;
    height: 860px;
    background: var(--paper);
    overflow: hidden;
  }
  .label__art {
    position: absolute;
    inset: 0;
    width: 680px;
    height: 860px;
  }
  .label__type-block {
    position: absolute;
    right: 18px;
    top: 38px;
    text-align: right;
    color: var(--paper);
    font-family: "Oswald", sans-serif;
    line-height: 1;
  }
  .label__type {
    font-size: 25px;
    font-weight: 500;
    letter-spacing: 0.2px;
  }
  .label__dose {
    font-size: 19px;
    font-weight: 400;
    margin-top: 10px;
  }
  .brand-name {
    position: absolute;
    left: 34px;
    top: 352px;
    font-family: "Questrial", sans-serif;
    font-size: 34px;
    color: var(--accent-orange);
    line-height: 1;
    letter-spacing: 0.5px;
  }
  .product-name {
    position: absolute;
    right: 32px;
    top: 540px;
    margin: 0;
    font-family: "Montserrat", sans-serif;
    font-weight: 600;
    font-size: 71px;
    color: var(--ink-grey);
    line-height: 1;
    letter-spacing: -0.5px;
  }
  .product-claim {
    position: absolute;
    right: 34px;
    top: 640px;
    margin: 0;
    text-align: right;
    font-family: "Questrial", sans-serif;
    font-size: 30px;
    line-height: 36px;
    color: var(--accent-orange);
    letter-spacing: 1px;
  }
  .product-count {
    position: absolute;
    right: 41px;
    top: 770px;
    margin: 0;
    font-family: "Questrial", sans-serif;
    font-size: 21px;
    color: var(--soft-grey);
    letter-spacing: 1px;
  }
</style>
</head>
<body>
  <main class="label">
    <svg class="label__art" viewBox="0 0 850 1075">
      <defs>
        <radialGradient id="hero-tone" cx="50%" cy="50%" r="55%">
          <stop offset="0%" stop-color="#d9d9d9"/>
          <stop offset="45%" stop-color="#c6c6c6"/>
          <stop offset="100%" stop-color="#eeeeee"/>
        </radialGradient>
      </defs>
      <path class="leaf-area" fill="var(--leaf-green)"
        role="img" aria-label="Large green leaf decoration sweeping across the top of the label"
        d="M0,0 H850 V688 C832,682 800,660 782,630 L560,500 L345,330
           C300,250 250,150 150,122 C85,108 35,130 0,125 Z"/>
      <circle class="hero-frame" cx="571" cy="378" r="232" fill="var(--paper)"/>
      <circle class="hero-ring" cx="571" cy="378" r="226" fill="none" stroke="var(--accent-orange)" stroke-width="12"/>
      <circle class="hero-image" cx="571" cy="378" r="211" fill="url(#hero-tone)"
        role="img" aria-label="Illustration of a human torso with the heart highlighted in red"/>
      <circle class="quality-badge" cx="151" cy="938" r="90" fill="var(--badge-green)"/>
    </svg>

    <div class="label__type-block">
      <div class="label__type">FOOD SUPPLEMENT</div>
      <div class="label__dose">1500mg</div>
    </div>

    <div class="brand-name">plumble tonic</div>

    <h1 class="product-name">Heart Heath</h1>
    <p class="product-claim">Premium Strength to<br>support healthy hearth</p>
    <p class="product-count">60 Tablets</p>
  </main>
</body>
</html>
```